We need a postcard design for a skin pathology laboratory in Long Beach, CA.( southern CA). We provide consultations on submitted specimens. Please see our website - www.corvellanhistology.example. Our clients are other physicians. Modern, clean design is desired.

Reason: Considering current designs and anticipating more submissions. Thank you.

Target Market(s)

Dermatologists, other physicians.

Industry/Entity Type

Laboratory

Requirements
Must have
• Name of company: Brambleton Tissue & Slide Review, Inc.
Address: 4817 Harwick Glen Ave. Suite 214, Long Beach, CA 90617.
Telephone # : 562 739 1046
website: www.corvellanhistology.example
Information regarding teaching/educational section of website.
Nice to have
• Nice fonts.

```html
<!DOCTYPE html>
<html lang="en">
<head>
<meta charset="utf-8">
<title>Brambleton Tissue &amp; Slide Review – Postcard</title>
<link rel="stylesheet" href="https://fonts.googleapis.com/css2?family=Cabin:wght@400;500&family=Cabin+Condensed:wght@500;600;700&display=swap">
<style>
  :root {
    --page-bg: #ececec;
    --tissue-light: #d9d6d6;
    --tissue-mid: #a7a2a3;
    --tissue-dark: #7d7779;
    --skin-light: #f2e4dc;
    --skin-mid: #e3c9bc;
    --ink: #1c1a1b;
    --band: #111011;
    --accent-red: #c0141c;
    --white: #ffffff;
  }
  * { box-sizing: border-box; margin: 0; padding: 0; }
  html, body { width: 1200px; height: 750px; overflow: hidden; }
  body { background: var(--page-bg); position: relative; }

  .postcard {
    position: absolute; left: 80px; top: 95px;
    width: 1040px; height: 560px; overflow: hidden;
    background: var(--tissue-light);
  }
  .tissue-backdrop {
    position: absolute; inset: 0;
    background:
      radial-gradient(ellipse 55% 70% at 62% 45%, var(--tissue-mid) 0%, rgba(167,162,163,0) 70%),
      radial-gradient(ellipse 35% 45% at 92% 30%, var(--tissue-dark) 0%, rgba(125,119,121,0) 75%),
      linear-gradient(160deg, #e4e1e1 0%, var(--tissue-light) 35%, #b4afb0 100%);
  }
  .hand-photo {
    position: absolute; left: 95px; top: 120px; width: 120px; height: 380px;
    border-radius: 50px 60px 0 0;
    background: linear-gradient(180deg, var(--skin-light) 0%, var(--skin-mid) 60%, #d8bcaf 100%);
    opacity: .9;
  }
  .callouts { position: absolute; inset: 0; }

  .company-name {
    position: absolute; left: 205px; top: 30px;
    font-family: "Cabin", sans-serif; font-weight: 500;
    font-size: 25px; letter-spacing: .5px; color: var(--ink);
    white-space: nowrap;
  }

  .message {
    position: absolute; left: 470px; top: 118px; width: 420px;
    text-align: center; color: var(--ink);
    font-family: "Cabin Condensed", sans-serif;
  }
  .message__headline {
    font-weight: 700; font-size: 25px; line-height: 1.5;
    text-transform: uppercase; letter-spacing: .3px;
  }
  .message__new {
    margin-top: 30px; font-weight: 600; font-size: 44px;
    color: var(--accent-red); line-height: 1;
  }
  .message__teaching {
    margin-top: 12px; font-weight: 700; font-size: 27px;
  }
  .message__url {
    font-family: "Cabin", sans-serif; font-weight: 500;
    font-size: 20px; color: var(--white); letter-spacing: .3px;
  }

  .contact-band {
    position: absolute; left: 0; right: 0; bottom: 0; height: 62px;
    background: var(--band); color: var(--white);
    font-family: "Cabin", sans-serif; font-size: 18px;
    display: flex; justify-content: space-between; align-items: center;
    padding: 0 28px;
  }
  .contact-band__phone { font-size: 21px; align-self: flex-end; padding-bottom: 12px; }
  .contact-band__address { align-self: flex-start; padding-top: 10px; }
</style>
</head>
<body>
  <section class="postcard">
    <div class="tissue-backdrop" role="img" aria-label="Grey microscope image of skin tissue filling the card background"></div>
    <div class="hand-photo" role="img" aria-label="Photograph of a raised open hand seen from the side"></div>

    <svg class="callouts" width="1040" height="560" viewBox="0 0 1040 560" aria-hidden="true">
      <line x1="0" y1="52" x2="195" y2="52" stroke="var(--ink)" stroke-width="1.2"/>
      <line x1="780" y1="52" x2="1010" y2="52" stroke="var(--ink)" stroke-width="1.2"/>
      <circle cx="1013" cy="52" r="4" fill="var(--ink)"/>

      <g stroke="var(--ink)" stroke-width="1.2">
        <line x1="180" y1="168" x2="300" y2="168"/>
        <line x1="180" y1="300" x2="300" y2="300"/>
        <line x1="180" y1="440" x2="300" y2="440"/>
      </g>
      <g fill="var(--ink)">
        <circle cx="180" cy="168" r="3.5"/>
        <circle cx="180" cy="300" r="3.5"/>
        <circle cx="180" cy="440" r="3.5"/>
      </g>
      <g stroke="var(--ink)" stroke-width="6">
        <circle cx="350" cy="160" r="52" fill="#b9b4b5" role="img" aria-label="Micrograph detail of skin cells"/>
        <circle cx="350" cy="295" r="52" fill="#c7c3c3" role="img" aria-label="Micrograph detail of tissue structure"/>
        <circle cx="350" cy="430" r="52" fill="#9e999a" role="img" aria-label="Micrograph detail of stained specimen"/>
      </g>
    </svg>

    <h1 class="company-name">Brambleton Tissue &amp; Slide Review, Inc.</h1>

    <div class="message">
      <p class="message__headline">Ready to support your practice<br>with exellent<br>dermatopathology consultations</p>
      <p class="message__new">New!</p>
      <p class="message__teaching">Teaching section on website</p>
      <p class="message__url">www.corvellanhistology.example</p>
    </div>

    <footer class="contact-band">
      <span class="contact-band__phone">P: 562 739 1046</span>
      <span class="contact-band__address">4817 Harwick Glen Ave. Suite 214, Long Beach, CA 90617</span>
    </footer>
  </section>
</body>
</html>
```